Electrician's Business needs web site for customers to get professional impression of business.

Have a logo, need a web page for customers to visit. Web page should make it easy for customers to approach /contact me, if possible a way for customers to leave their details so I can call them back.
A description/ list of services and advertise how my service is different and better than other electricians.
A gallery to upload photos to, to show completed works from past projects.

Target Market(s)

Domestic/residential home owner/renter/builder

Industry/Entity Type

Electrician

Coding

Coded - Design and coding required

Number of Pages Required

2 page

Font styles to use
Sans Serif

Colors
0255a3
ffffff

Requirements
Must have
• Appeal to home owner/renter, domestic market.
• Capture contact details of customer & advertise my contact details.
• List of services
Nice to have
• A photo gallery, so I can upload pictures of completed work.
Should not have
• Industrial/construction images.

```html
<!DOCTYPE html>
<html lang="en">
<head>
<meta charset="utf-8">
<title>Brightline – Electrician Service</title>
<link href="https://fonts.googleapis.com/css2?family=Roboto:wght@300;400;500;700&display=swap" rel="stylesheet">
<style>
:root{
  --blue:#0255a3;
  --blue-dark:#023f7a;
  --blue-deep:#01305e;
  --orange:#f47b20;
  --white:#ffffff;
  --ink:#333a44;
  --muted:#7b818a;
  --grey-bg:#f1f2f4;
  --line:#dfe2e6;
}
*{box-sizing:border-box;margin:0;padding:0}
html,body{width:1200px;height:2632px;overflow:hidden}
body{font-family:'Roboto',Arial,sans-serif;color:var(--ink);background:var(--white);font-size:14px;line-height:1.6}
a{color:inherit;text-decoration:none}

/* header */
.site-header{height:112px;background:var(--blue);color:var(--white);position:relative}
.brand{position:absolute;left:84px;top:18px}
.brand-name{font-size:40px;font-weight:700;line-height:1;letter-spacing:-0.5px}
.brand-tag{font-size:15px;color:var(--orange);font-weight:500;margin-top:4px;padding-left:40px}
.quick-contact{position:absolute;right:52px;top:12px;font-size:13px;display:flex;align-items:center;gap:14px}
.quick-contact .sep{opacity:.6}
.social{display:flex;gap:8px}
.social span{width:20px;height:20px;border-radius:50%;background:rgba(255,255,255,.25)}
.main-nav{position:absolute;right:52px;top:60px;display:flex;gap:38px;font-size:14px;font-weight:500}
.main-nav a{padding-bottom:10px}
.main-nav a.active{border-bottom:2px solid var(--white)}

/* hero */
.hero{height:488px;position:relative;background:linear-gradient(110deg,#e9edf1 0%,#cfd6de 45%,#9aa7b4 75%,#6f7b88 100%)}
.hero-caption{position:absolute;left:136px;top:364px}
.hero-caption h1{font-size:48px;color:var(--orange);font-weight:400;line-height:1.05}
.hero-caption p{font-size:36px;color:var(--blue);font-weight:400;line-height:1.1}
.slide-arrow{position:absolute;top:222px;width:32px;height:44px;background:rgba(0,0,0,.35);display:flex;align-items:center;justify-content:center}
.slide-arrow.prev{left:36px}.slide-arrow.next{right:36px}

/* welcome */
.welcome{height:460px;position:relative}
.welcome-img{position:absolute;left:88px;top:140px;width:224px;height:172px;background:linear-gradient(135deg,#8fa4b8,#3c5875)}
.welcome-text{position:absolute;left:340px;top:146px;width:780px}
.welcome-text h2{font-size:22px;font-weight:500;color:var(--ink);letter-spacing:.5px;line-height:1.3}
.welcome-text h2 b{color:var(--blue);font-weight:500}
.welcome-text .lead{color:var(--blue);font-size:15px;margin-bottom:8px}
.welcome-text p{font-size:11px;color:var(--muted);line-height:1.55;margin-bottom:8px}
.btn-orange{display:inline-block;background:var(--orange);color:var(--white);font-size:11px;font-weight:500;padding:4px 14px;border-radius:2px;margin-top:4px}

/* section heads */
.section-head{text-align:center}
.section-head h2{font-size:26px;font-weight:500;color:var(--ink);letter-spacing:.5px;line-height:1.3}
.section-head h2 b{color:var(--blue);font-weight:500}
.section-head p{font-size:12px;color:var(--muted)}

/* services */
.services{height:480px;background:var(--grey-bg);padding-top:76px}
.service-list{display:flex;justify-content:center;gap:26px;margin-top:104px}
.service{width:250px;text-align:center}
.service svg{width:34px;height:34px}
.service h3{font-size:13px;font-weight:500;margin:12px 0 8px;letter-spacing:.3px}
.service p{font-size:10.5px;color:var(--muted);line-height:1.5;padding:0 18px}
.btn-outline{display:inline-block;margin-top:16px;font-size:11px;border:1px solid #b9bec5;background:var(--white);padding:3px 14px;border-radius:2px}

/* gallery */
.gallery{height:500px;padding-top:96px}
.gallery-strip{display:flex;margin-top:34px;height:300px}
.gallery-strip div{flex:1}
.g1{background:linear-gradient(135deg,#c7b9a8,#6d6458)}
.g2{background:linear-gradient(135deg,#9fa9b1,#4d5861)}
.g3{background:linear-gradient(135deg,#b7c2cb,#5d6f7f)}
.g4{background:linear-gradient(135deg,#d2c4b0,#7d6a54)}
.g5{background:linear-gradient(135deg,#aab6c0,#3e4e5d)}

/* blog */
.blog{height:296px;position:relative;padding:26px 88px 0}
.blog-head{display:flex;justify-content:space-between;align-items:center}
.blog-head h2{font-size:22px;font-weight:500}
.blog-head h2 b{color:var(--blue);font-weight:500}
.blog-arrows{font-size:20px;color:var(--muted);letter-spacing:10px}
.posts{display:flex;gap:40px;margin-top:20px}
.post{display:flex;gap:20px;width:492px}
.post-img{width:216px;height:150px;flex:none}
.post:nth-child(1) .post-img{background:linear-gradient(135deg,#c9b49c,#5d4c3d)}
.post:nth-child(2) .post-img{background:linear-gradient(135deg,#b4c1cd,#4a6076)}
.post h4{font-size:12px;font-weight:500;margin-top:4px}
.post .date{font-size:10px;color:var(--orange)}
.post p{font-size:10.5px;color:var(--muted);line-height:1.5;margin-top:4px}
.post .more{font-size:10.5px;color:var(--blue);margin-top:8px;display:block}

/* footer */
.site-footer{height:264px;background:var(--blue);color:var(--white);padding:34px 88px 0;display:flex;gap:40px}
.foot-col h5{font-size:12px;font-weight:500;letter-spacing:.5px;margin-bottom:14px}
.foot-col li{list-style:none;font-size:10.5px;line-height:2;opacity:.9}
.foot-col li::before{content:"› ";}
.foot-col p{font-size:10.5px;line-height:2;opacity:.9}
.links{width:130px}
.location{width:180px}
.map{width:180px;height:110px;background:linear-gradient(135deg,#e5e7e0,#c7ccc0)}
.touch{width:230px}
.follow{width:150px}
.follow .social{margin-top:12px}
.follow .social span{width:28px;height:28px;background:rgba(255,255,255,.2)}
.callback{width:190px}
.callback-form{display:flex;flex-direction:column;gap:7px}
.callback-form input{height:26px;border:1px solid rgba(255,255,255,.35);background:rgba(255,255,255,.12);color:var(--white);font:400 11px 'Roboto',Arial,sans-serif;padding:0 8px;border-radius:2px}
.callback-form input::placeholder{color:rgba(255,255,255,.75)}
.callback-form button{height:26px;border:0;background:var(--orange);color:var(--white);font:500 11px 'Roboto',Arial,sans-serif;letter-spacing:.4px;border-radius:2px}
.copyright{height:32px;background:var(--blue-deep);color:rgba(255,255,255,.75);font-size:10px;text-align:center;line-height:32px;position:relative}
.copyright .top{position:absolute;right:20px;top:0}
</style>
</head>
<body>

<header class="site-header">
  <div class="brand">
    <div class="brand-name">Brightline</div>
    <div class="brand-tag">Electrical Services</div>
  </div>
  <div class="quick-contact">
    <span>QUICK CONTACT</span><span class="sep">|</span><span>(555) 214 0386</span>
    <div class="social"><span></span><span></span><span></span></div>
  </div>
  <nav class="main-nav">
    <a class="active" href="#">HOME</a><a href="#">ABOUT US</a><a href="#">SERVICES</a><a href="#">PROJECTS</a><a href="#">BLOG</a><a href="#">CLIENTS</a><a href="#">CONTACT</a>
  </nav>
</header>

<section class="hero" role="img" aria-label="Electrician in a hard hat stripping a cable with pliers">
  <div class="slide-arrow prev"><svg width="12" height="18" viewBox="0 0 12 18"><path d="M10 2L3 9l7 7" stroke="#fff" stroke-width="2.5" fill="none"/></svg></div>
  <div class="slide-arrow next"><svg width="12" height="18" viewBox="0 0 12 18"><path d="M2 2l7 7-7 7" stroke="#fff" stroke-width="2.5" fill="none"/></svg></div>
  <div class="hero-caption">
    <h1>BRIGHTLINE</h1>
    <p>Electrician service</p>
  </div>
</section>

<section class="welcome">
  <div class="welcome-img" role="img" aria-label="Electrician working at a switchboard panel"></div>
  <div class="welcome-text">
    <h2>WELCOME TO <b>BRIGHTLINE</b></h2>
    <div class="lead">Safe, tidy and reliable electrical work for your home, done right first time</div>
    <p>We are a local, fully licensed team looking after home owners, renters and builders. Every job is quoted up front, with no hidden costs, and our electricians arrive on time, explain the work clearly and leave your home clean when they finish.</p>
    <p>From a single new power point to a full rewire, we test every circuit and back our work with a written guarantee. Call us or leave your details and we will ring you back the same day to arrange a time that suits you.</p>
    <a class="btn-orange" href="#">READ MORE</a>
  </div>
</section>

<section class="services">
  <div class="section-head">
    <h2>OUR <b>SERVICES</b></h2>
    <p>Everything your home needs, from quick repairs to new installations and safety checks</p>
  </div>
  <div class="service-list">
    <div class="service">
      <svg viewBox="0 0 24 24"><path d="M12 3L2 12h3v8h5v-5h4v5h5v-8h3z" fill="var(--orange)"/></svg>
      <h3>DOMESTIC</h3>
      <p>Lighting, power points, switchboards and fault finding for every room of your home.</p>
      <a class="btn-outline" href="#">Read More</a>
    </div>
    <div class="service">
      <svg viewBox="0 0 24 24"><rect x="5" y="2" width="14" height="20" rx="1" fill="var(--orange)"/><rect x="8" y="5" width="3" height="3" fill="#fff"/><rect x="13" y="5" width="3" height="3" fill="#fff"/><rect x="8" y="10" width="3" height="3" fill="#fff"/><rect x="13" y="10" width="3" height="3" fill="#fff"/></svg>
      <h3>COMMERCIAL</h3>
      <p>Shops and offices kept running with safe wiring, tidy cabling and quick call outs.</p>
      <a class="btn-outline" href="#">Read More</a>
    </div>
    <div class="service">
      <svg viewBox="0 0 24 24"><circle cx="12" cy="12" r="6" fill="none" stroke="var(--orange)" stroke-width="4"/><path d="M12 1v5M12 18v5M1 12h5M18 12h5M4 4l3.5 3.5M16.5 16.5L20 20M4 20l3.5-3.5M16.5 7.5L20 4" stroke="var(--orange)" stroke-width="3"/></svg>
      <h3>INDUSTRIAL SECTORS</h3>
      <p>Three phase power, machine connections and testing for workshops and sites.</p>
      <a class="btn-outline" href="#">Read More</a>
    </div>
    <div class="service">
      <svg viewBox="0 0 24 24"><path d="M8 2v5M16 2v5M5 7h14v4a7 7 0 0 1-14 0zM12 18v4" stroke="var(--orange)" stroke-width="3" fill="var(--orange)"/></svg>
      <h3>ELECTRICIAN</h3>
      <p>Licensed electricians on call for repairs, upgrades and emergency work.</p>
      <a class="btn-outline" href="#">Read More</a>
    </div>
  </div>
</section>

<section class="gallery">
  <div class="section-head">
    <h2>OUR <b>GALLERY</b></h2>
    <p>A look at some of the jobs we have completed for our customers</p>
  </div>
  <div class="gallery-strip">
    <div class="g1" role="img" aria-label="Completed switchboard installation"></div>
    <div class="g2" role="img" aria-label="Wiring inside a distribution cabinet"></div>
    <div class="g3" role="img" aria-label="Electrician checking plans on site"></div>
    <div class="g4" role="img" aria-label="Electrician fitting a light fixture"></div>
    <div class="g5" role="img" aria-label="Finished electrical panel"></div>
  </div>
</section>

<section class="blog">
  <div class="blog-head">
    <h2>LATEST <b>BLOG</b></h2>
    <div class="blog-arrows">‹ ›</div>
  </div>
  <div class="posts">
    <article class="post">
      <div class="post-img" role="img" aria-label="Electrician testing a home circuit"></div>
      <div>
        <h4>SIMPLE SAFETY TIPS</h4>
        <div class="date">22 July 2016</div>
        <p>Simple checks every home owner can do to spot faulty outlets, worn cords and overloaded power boards before they cause trouble.</p>
        <a class="more" href="#">Read More ›</a>
      </div>
    </article>
    <article class="post">
      <div class="post-img" role="img" aria-label="Electrician repairing a wall socket"></div>
      <div>
        <h4>SIMPLE SAFETY TIPS</h4>
        <div class="date">22 July 2016</div>
        <p>When to upgrade your switchboard and how modern safety switches protect your family from shocks and electrical fires.</p>
        <a class="more" href="#">Read More ›</a>
      </div>
    </article>
  </div>
</section>

<footer class="site-footer">
  <div class="foot-col links">
    <h5>LINKS</h5>
    <ul><li>Who we are</li><li>How we work</li><li>Skills</li><li>Projects</li><li>Blog</li></ul>
  </div>
  <div class="foot-col location">
    <h5>LOCATION</h5>
    <div class="map" role="img" aria-label="Street map showing the business location"></div>
  </div>
  <div class="foot-col touch">
    <h5>GET IN TOUCH</h5>
    <p>Address : 2841 Harbor Lane,<br>Northfield NE 68104</p>
    <p>Phone : (555) 214 0386</p>
    <p>Email : hello@brightline-electric.com</p>
  </div>
  <div class="foot-col follow">
    <h5>FOLLOW US</h5>
    <p>Connect with our social network</p>
    <div class="social"><span></span><span></span><span></span></div>
  </div>
  <div class="foot-col callback">
    <h5>REQUEST A CALLBACK</h5>
    <form class="callback-form" action="#" method="post">
      <input type="text" name="name" placeholder="Your name" aria-label="Your name">
      <input type="tel" name="phone" placeholder="Phone number" aria-label="Phone number">
      <input type="text" name="job" placeholder="What do you need?" aria-label="What do you need">
      <button type="submit">CALL ME BACK</button>
    </form>
  </div>
</footer>
<div class="copyright">Copyright © 2016. All Rights Reserved <span class="top">⌃</span></div>

</body>
</html>
```